Modern Innovative Business Card Design

We require a nice, modern, clean business card design, ready for upload to Cardomora. Our company develops online banking software solutions for small financial insitutions. The design should be clean, professional, but yet not "corporate boring". See www.fyrolt.com for an idea of business image and profile. The design should communicate innovation, be modern and fresh, yet look professional and established.

Target Market(s)

Finance industry, bankers, entrepreneurs

Industry/Entity Type

Financial

Contact Information for Business Card

Tobias Wendlerup
CEO

FYROLT BV
Lindenwerf 38
1027 HX Amsterdam
The Netherlands

Phone: +31 20 517 8036
Direct: +31 20 604 1758
chat: tobias.fyrolt
ceo@fyrolt.com
www.fyrolt.com

Font styles to use
Sans Serif

Requirements
Must have
• Should look clean, modern and professional. File should be ready for upload to cardomora.
Should not have
• Boring standard corporate layout

```html
<!DOCTYPE html>
<html lang="en">
<head>
<meta charset="utf-8">
<title>FYROLT Business Card</title>
<link rel="stylesheet" href="https://fonts.googleapis.com/css2?family=Arimo:wght@400;700&family=Tinos:wght@700&display=swap">
<style>
  :root {
    --page-bg: #e9e6e1;
    --card-dark: #050505;
    --card-light: #ffffff;
    --brand-green: #8cc63f;
    --brand-grey: #6f6f6f;
    --ink: #111111;
    --shadow: rgba(0, 0, 0, 0.22);
  }
  * { box-sizing: border-box; margin: 0; padding: 0; }
  html, body {
    width: 1200px;
    height: 800px;
    overflow: hidden;
    background: var(--page-bg);
  }
  .sheet {
    width: 1200px;
    height: 800px;
    display: flex;
    align-items: center;
    justify-content: center;
    gap: 60px;
  }
  .card {
    width: 480px;
    height: 480px;
    border-radius: 4px;
    box-shadow: 0 14px 34px var(--shadow);
    position: relative;
  }
  .card--front {
    background: var(--card-dark);
    display: flex;
    align-items: center;
    justify-content: center;
  }
  .wordmark {
    font-family: "Arimo", Arial, sans-serif;
    font-weight: 400;
    font-size: 64px;
    letter-spacing: 10px;
    color: var(--brand-green);
  }
  .card--back {
    background: var(--card-light);
    padding: 56px 44px 40px 48px;
  }
  .holder-name {
    font-family: "Tinos", "Times New Roman", serif;
    font-weight: 700;
    font-size: 38px;
    color: var(--brand-green);
    text-align: right;
    line-height: 1;
  }
  .holder-role {
    font-family: "Arimo", Arial, sans-serif;
    font-size: 18px;
    color: var(--ink);
    margin-top: 6px;
    margin-left: 4px;
  }
  .contact-list {
    list-style: none;
    margin-top: 40px;
    font-family: "Arimo", Arial, sans-serif;
    font-size: 22px;
    line-height: 1.2;
    color: var(--ink);
  }
  .contact-item {
    display: flex;
    align-items: flex-start;
    gap: 22px;
    margin-bottom: 8px;
  }
  .contact-icon {
    flex: 0 0 24px;
    width: 24px;
    height: 24px;
    margin-top: 2px;
  }
  .contact-icon rect.badge { fill: var(--brand-green); }
  .contact-icon .glyph { fill: none; stroke: #1f3a08; stroke-width: 1.6; stroke-linecap: round; stroke-linejoin: round; }
  .contact-icon .glyph-fill { fill: #1f3a08; }
</style>
</head>
<body>
<main class="sheet">
  <section class="card card--front" aria-label="Card front">
    <span class="wordmark">FYROLT</span>
  </section>

  <section class="card card--back" aria-label="Card back">
    <h1 class="holder-name">Tobias Wendlerup</h1>
    <p class="holder-role">CEO FYROLT BV</p>

    <ul class="contact-list">
      <li class="contact-item">
        <svg class="contact-icon" viewBox="0 0 24 24" aria-hidden="true">
          <rect class="badge" width="24" height="24" rx="2"/>
          <path class="glyph" d="M6 9c0-2 2-3 6-3s6 1 6 3l-2 1-1-2h-6l-1 2zM8 12h8v6H8z"/>
        </svg>
        <span>+31 20 517 8036</span>
      </li>
      <li class="contact-item">
        <svg class="contact-icon" viewBox="0 0 24 24" aria-hidden="true">
          <rect class="badge" width="24" height="24" rx="2"/>
          <rect class="glyph" x="8" y="4" width="8" height="16" rx="1.5"/>
          <path class="glyph" d="M10 17h4"/>
        </svg>
        <span>+31 20 604 1758</span>
      </li>
      <li class="contact-item">
        <svg class="contact-icon" viewBox="0 0 24 24" aria-hidden="true">
          <rect class="badge" width="24" height="24" rx="2"/>
          <path class="glyph" d="M5 12l7-6 7 6M7 11v7h10v-7M11 18v-4h2v4"/>
        </svg>
        <span>Lindenwerf 38<br>1027 HX Amsterdam<br>The Netherlands</span>
      </li>
      <li class="contact-item">
        <svg class="contact-icon" viewBox="0 0 24 24" aria-hidden="true">
          <rect class="badge" width="24" height="24" rx="2"/>
          <rect class="glyph" x="5" y="7" width="14" height="10"/>
          <path class="glyph" d="M5 7l7 6 7-6"/>
        </svg>
        <span>ceo@fyrolt.com</span>
      </li>
      <li class="contact-item">
        <svg class="contact-icon" viewBox="0 0 24 24" aria-hidden="true">
          <rect class="badge" width="24" height="24" rx="2"/>
          <circle class="glyph" cx="12" cy="12" r="6.5"/>
          <path class="glyph" d="M5.5 12h13M12 5.5c-3 3.5-3 9.5 0 13M12 5.5c3 3.5 3 9.5 0 13"/>
        </svg>
        <span>www.fyrolt.com</span>
      </li>
      <li class="contact-item">
        <svg class="contact-icon" viewBox="0 0 24 24" aria-hidden="true">
          <rect class="badge" width="24" height="24" rx="2"/>
          <circle class="glyph-fill" cx="12" cy="12" r="6"/>
        </svg>
        <span>tobias.fyrolt</span>
      </li>
    </ul>
  </section>
</main>
</body>
</html>
```